Wine Bottle Label Graphic Design (mini bottle 187ml)

Looking for a contemporary custom wine label design for party favors. Inspiration photos provided. **Please see "wine favorite" example in uploads.

Artwork 2.5" wide by 2.75" tall to be placed on 3"x3" stickers. Specs from printer attached but I still want image to fit within the artwork size I specified. Please make label center justified. This is for BOYS. It does not need to be super "masculine"...but definitely not feminine.

Required elements:

Colors: white background, include gold and purple to match logo. Other colors are fine to include.

Name: Sababa 13 (I like use of the No) as shown in the sample, but not required
Varietal: Mitzvah Blend 6.11.2021
Vineyard: Hollis Family Vineyard
Location: Maryland
Logo: See attached (KRNotecard Final)

Font styles to use
Serif
Sans Serif

Requirements
Must have
• All the above elements. Clean and crisp design. Contemporary and classy. Purple, Gold, Black colors. See logo. You CAN include cursive font for select elements. I don't mind a combination of print and script.
Should not have
• Floral, scrolling, background image, old fashioned

```html
<!DOCTYPE html>
<html lang="en">
<head>
<meta charset="utf-8">
<title>Sababa 13 – Mitzvah Blend Labels</title>
<link rel="stylesheet" href="https://fonts.googleapis.com/css2?family=Chewy&family=Special+Elite&family=Playfair+Display:wght@700&family=Montserrat:wght@700&family=Libre+Baskerville:wght@700&display=swap">
<style>
  :root {
    --purple: #4a2a72;
    --gold-light: #fbf1b8;
    --gold: #e6c25a;
    --gold-deep: #d49a2a;
    --label-white: #ffffff;
    --backdrop: #2b2b2b;
  }
  * { margin: 0; padding: 0; box-sizing: border-box; }
  html, body { width: 1200px; height: 900px; overflow: hidden; }
  body { background: var(--backdrop); position: relative; }

  .label {
    position: absolute;
    top: 232px;
    width: 434px;
    height: 434px;
    background: var(--label-white);
  }
  .label--brush { left: 131px; }
  .label--type { left: 637px; }

  .label__frame {
    position: absolute;
    left: 33px; top: 16px; right: 33px; bottom: 16px;
    border: 4px solid var(--gold);
    border-image: linear-gradient(135deg, var(--gold-light), var(--gold-deep) 35%, var(--gold-light) 60%, var(--gold-deep)) 1;
  }

  .brand {
    position: absolute;
    top: 30px; left: 0; right: 0;
    display: flex; flex-direction: column; align-items: center; gap: 6px;
  }
  .brand__dot {
    width: 58px; height: 58px; border-radius: 50%;
    background: var(--purple);
  }
  .brand__name {
    font-family: "Montserrat", sans-serif;
    font-weight: 700; font-size: 11px; letter-spacing: 2px;
    color: var(--purple);
  }

  .star-art {
    position: absolute;
    left: 104px; top: 142px; width: 226px; height: 206px;
    background: radial-gradient(ellipse at 50% 55%, var(--gold) 0%, var(--gold-light) 55%, rgba(251,241,184,0) 75%);
  }
  .label--type .star-art { left: 110px; top: 152px; width: 232px; height: 212px; }

  .title {
    position: absolute; left: 0; right: 0;
    text-align: center; color: var(--purple); line-height: 1;
  }
  .label--brush .title__name {
    top: 150px; font-family: "Chewy", cursive; font-size: 70px;
  }
  .label--brush .title__number {
    top: 258px; font-family: "Playfair Display", serif; font-weight: 700; font-size: 50px;
  }
  .label--type .title__name {
    top: 182px; font-family: "Special Elite", monospace; font-size: 50px;
  }
  .label--type .title__number {
    top: 246px; font-family: "Special Elite", monospace; font-size: 44px;
  }

  .details {
    position: absolute; left: 0; right: 0; top: 318px;
    text-align: center; color: var(--purple);
    font-family: "Montserrat", sans-serif; font-weight: 700;
  }
  .details__varietal { font-size: 9px; letter-spacing: 1px; line-height: 14px; }
  .details__year { font-size: 11px; letter-spacing: 1.5px; line-height: 14px; }
  .details__rule {
    width: 126px; height: 2px; background: var(--purple);
    margin: 8px auto 7px;
  }
  .label--type .details__rule { width: 156px; }
  .details__vineyard { font-size: 11px; letter-spacing: 1px; line-height: 15px; }
  .label--type .details__vineyard { font-size: 12px; letter-spacing: 2px; }
  .details__region { font-size: 9px; line-height: 13px; }
  .label--brush .details__region { font-family: "Libre Baskerville", serif; text-transform: none; }
  .label--type .details__region { letter-spacing: 2px; font-size: 10px; }
</style>
</head>
<body>

  <section class="label label--brush">
    <div class="label__frame"></div>
    <div class="brand">
      <span class="brand__dot"></span>
      <span class="brand__name">KIRA &amp; ROWAN</span>
    </div>
    <div class="star-art" role="img" aria-label="Gold brush-stroke Star of David"></div>
    <h1 class="title title__name">Sababa</h1>
    <p class="title title__number">№13</p>
    <div class="details">
      <p class="details__varietal">MITZVAH BLEND</p>
      <p class="details__year">2021</p>
      <div class="details__rule"></div>
      <p class="details__vineyard">HOLLIS FAMILY VINEYARD</p>
      <p class="details__region">Maryland</p>
    </div>
  </section>

  <section class="label label--type">
    <div class="label__frame"></div>
    <div class="brand">
      <span class="brand__dot"></span>
      <span class="brand__name">KIRA &amp; ROWAN</span>
    </div>
    <div class="star-art" role="img" aria-label="Gold brush-stroke Star of David"></div>
    <h1 class="title title__name">Sababa</h1>
    <p class="title title__number">№13</p>
    <div class="details">
      <p class="details__varietal">MITZVAH BLEND</p>
      <p class="details__year">2021</p>
      <div class="details__rule"></div>
      <p class="details__vineyard">HOLLIS FAMILY VINEYARD</p>
      <p class="details__region">MARYLAND</p>
    </div>
  </section>

</body>
</html>
```